The Shamblers

Copper Heron Productions is looking for their theatrical poster for their film 'THE SHAMBLERS'... It is a zombie appocalypse action film made in NSW Australia. See their facebook page www.pagebook.example/THEDRIFTERSFILM...
Updates
Project Deadline Extended
Reason: i have decided to EXTEND the deadline for 5 more days, as there are some really talented artists reviewing their submissions for us... Thank you to all...
Please review the new uploaded images you may or may not want to use to revierw your submissions
Logo Text
Copper Heron Productions
Look and feel
Each slider illustrates characteristics of the customer's brand and the style your logo design should communicate.

```html
<!DOCTYPE html>
<html lang="en">
<head>
<meta charset="utf-8">
<title>The Shamblers – Theatrical Poster</title>
<link rel="stylesheet" href="https://fonts.googleapis.com/css2?family=Anton&display=swap">
<style>
  :root {
    --backdrop: #bdbdbd;
    --paper: #f4f4f3;
    --paper-shade: #dcdcdc;
    --blood: #b5131b;
    --blood-dark: #8a0f13;
    --blood-deep: #6e0a0d;
    --ink: #111111;
  }
  * { margin: 0; padding: 0; box-sizing: border-box; }
  html, body {
    width: 1200px;
    height: 1000px;
    overflow: hidden;
    background: var(--backdrop);
  }
  .canvas {
    position: relative;
    width: 1200px;
    height: 1000px;
  }
  .poster {
    position: absolute;
    left: 277px;
    top: 38px;
    width: 645px;
    height: 924px;
    overflow: hidden;
    background:
      radial-gradient(ellipse at 30% 40%, rgba(255,255,255,0.9), transparent 60%),
      radial-gradient(ellipse at 80% 20%, var(--paper-shade), transparent 55%),
      radial-gradient(ellipse at 20% 85%, var(--paper-shade), transparent 50%),
      var(--paper);
    font-family: "Anton", "Impact", sans-serif;
    color: var(--ink);
  }
  .walking-figure {
    position: absolute;
    left: 72px;
    top: 0;
    width: 180px;
    height: 432px;
    background: linear-gradient(180deg, var(--blood) 0%, #8e1014 60%, var(--blood-deep) 100%);
    border-radius: 0 0 40px 20px;
  }
  .blood-ring {
    position: absolute;
    left: 0;
    top: 0;
    width: 645px;
    height: 924px;
  }
  .director-credit {
    position: absolute;
    left: 275px;
    top: 172px;
    font-size: 36px;
    line-height: 1.02;
    letter-spacing: 1px;
    text-transform: uppercase;
  }
  .film-title {
    font-weight: 400;
  }
  .title-block {
    position: absolute;
    left: 93px;
    width: 463px;
    text-align: center;
    text-transform: uppercase;
    line-height: 1;
    white-space: nowrap;
  }
  .title-article {
    top: 377px;
    font-size: 60px;
    letter-spacing: 2px;
    color: var(--blood-dark);
  }
  .title-main {
    top: 446px;
    font-size: 118px;
    letter-spacing: 1px;
    color: var(--blood);
  }
  .title-rule {
    position: absolute;
    left: 101px;
    width: 455px;
    height: 3px;
    background: var(--blood);
  }
  .title-rule--upper { top: 571px; }
  .title-rule--lower { top: 669px; }
  .tagline {
    position: absolute;
    left: 101px;
    top: 578px;
    font-size: 38px;
    line-height: 1.08;
    white-space: nowrap;
  }
  .cast-list {
    position: absolute;
    left: 106px;
    top: 768px;
    width: 445px;
    display: flex;
    justify-content: space-between;
    list-style: none;
    font-size: 15px;
    text-transform: uppercase;
    letter-spacing: 0.3px;
  }
</style>
</head>
<body>
<div class="canvas">
  <div class="poster">
    <div class="walking-figure" role="img" aria-label="Red silhouette of a person walking, seen from the waist down"></div>

    <svg class="blood-ring" viewBox="0 0 645 924" aria-hidden="true">
      <circle cx="480" cy="850" r="165" fill="none" stroke="var(--blood)" stroke-width="50" opacity="0.85"/>
      <circle cx="480" cy="850" r="138" fill="var(--paper)" opacity="0.6"/>
      <circle cx="235" cy="840" r="7" fill="var(--blood)"/>
      <circle cx="262" cy="844" r="9" fill="var(--blood)"/>
      <circle cx="90" cy="725" r="3" fill="var(--blood)"/>
      <circle cx="110" cy="735" r="2" fill="var(--blood)"/>
    </svg>

    <p class="director-credit">A film by<br>Declan Hale</p>

    <h1 class="film-title">
      <span class="title-block title-article">The</span>
      <span class="title-block title-main">Shamblers</span>
    </h1>

    <div class="title-rule title-rule--upper"></div>
    <p class="tagline">find a cure,<br>before it takes over the world</p>
    <div class="title-rule title-rule--lower"></div>

    <ul class="cast-list">
      <li>Declan Hale -</li>
      <li>Marco Vellini</li>
      <li>Sienna Marlow</li>
      <li>Tia Brennan</li>
    </ul>
  </div>
</div>
</body>
</html>
```